New Flyer Design Project

I would like to purchase a customized version of a design you have previously submitted - https://www.artmarketly.com/design/58210947
hi
would like the design about the some. just with our  details and logo
office number 01394528160
Mobil number 07821563047
web lunarsweep.ltd
email lunarsweep@postmerin.co.uk
on the back we would like to put a price list

```html
<!DOCTYPE html>
<html lang="en">
<head>
<meta charset="utf-8">
<title>Lunar Sweep – Window Cleaning in Essex</title>
<link href="https://fonts.googleapis.com/css2?family=Montserrat:wght@400;500;600;700;800;900&display=swap" rel="stylesheet">
<style>
  :root {
    --navy: #2b3990;
    --blue: #3c8ad5;
    --blue-deep: #2f76c4;
    --sky: #8ec8f0;
    --white: #ffffff;
    --ink: #1b1f3b;
    --photo-brick: #8a4b3a;
    --photo-green: #4d6b34;
  }
  html, body {
    margin: 0;
    padding: 0;
    width: 900px;
    height: 1200px;
    overflow: hidden;
    background: var(--white);
  }
  .flyer {
    position: relative;
    width: 900px;
    height: 1200px;
    overflow: hidden;
    font-family: "Montserrat", sans-serif;
    color: var(--ink);
  }
  .flyer-art {
    position: absolute;
    inset: 0;
    width: 900px;
    height: 1200px;
  }
  .brand {
    position: absolute;
    left: 53px;
    top: 46px;
    width: 270px;
    text-align: center;
    line-height: 1;
  }
  .brand-name {
    display: block;
    font-size: 37px;
    font-weight: 800;
    letter-spacing: -1px;
    color: var(--blue-deep);
  }
  .brand-sub {
    display: block;
    font-size: 15.5px;
    font-weight: 500;
    margin-top: 12px;
    color: var(--navy);
    white-space: nowrap;
  }
  .section-title {
    position: absolute;
    left: 29px;
    margin: 0;
    font-size: 16px;
    font-weight: 900;
    color: var(--sky);
    letter-spacing: 0.2px;
    line-height: 1;
  }
  .about-title { top: 711px; }
  .why-title { top: 930px; }
  .body-copy {
    position: absolute;
    left: 27px;
    margin: 0;
    font-size: 11.6px;
    line-height: 14.4px;
    color: var(--white);
    font-weight: 500;
  }
  .about-copy-1 { top: 743px; }
  .about-copy-2 { top: 829px; }
  .why-copy { top: 962px; }
  .benefits {
    position: absolute;
    left: 27px;
    top: 1014px;
    margin: 0;
    padding: 0;
    list-style: none;
    color: var(--white);
    font-size: 10.6px;
    font-weight: 700;
    line-height: 18.2px;
  }
  .benefits li {
    display: flex;
    align-items: center;
    gap: 5px;
  }
  .benefits svg { width: 12px; height: 12px; flex: none; }
  .headline {
    position: absolute;
    left: 480px;
    width: 396px;
    top: 584px;
    text-align: center;
    margin: 0;
  }
  .headline-kicker {
    display: block;
    color: var(--blue-deep);
    font-weight: 800;
    font-size: 21.5px;
    line-height: 27px;
    letter-spacing: -0.3px;
  }
  .headline-main {
    display: block;
    font-weight: 900;
    font-size: 70px;
    line-height: 62px;
    letter-spacing: -3px;
    color: var(--navy);
    margin-top: 4px;
  }
  .headline-main.accent { color: var(--blue); }
  .offer {
    position: absolute;
    left: 470px;
    width: 416px;
    top: 853px;
    margin: 0;
    text-align: center;
    font-size: 16.2px;
    line-height: 18px;
    font-weight: 500;
    color: var(--ink);
  }
  .cta {
    position: absolute;
    left: 544px;
    top: 957px;
    width: 266px;
    height: 40px;
    border-radius: 14px;
    background: var(--navy);
    color: var(--white);
    font-weight: 900;
    font-size: 19.5px;
    display: flex;
    align-items: center;
    justify-content: center;
    letter-spacing: 0.3px;
  }
  .contact-list {
    position: absolute;
    left: 548px;
    top: 1004px;
    width: 352px;
    margin: 0;
    padding: 0;
    list-style: none;
  }
  .contact-list li {
    height: 28px;
    display: flex;
    align-items: center;
    gap: 6px;
    padding-left: 9px;
    font-size: 14.5px;
    font-weight: 700;
    color: var(--ink);
    border-bottom: 1.5px dashed var(--blue);
  }
  .contact-list li:last-child { border-bottom: none; }
  .contact-list svg { width: 11px; height: 11px; flex: none; }
  .website {
    position: absolute;
    left: 0;
    width: 900px;
    top: 1148px;
    text-align: center;
    margin: 0;
    font-size: 22px;
    font-weight: 700;
    color: var(--navy);
  }
</style>
</head>
<body>
<div class="flyer">
  <svg class="flyer-art" viewBox="0 0 900 1200" xmlns="http://www.w3.org/2000/svg">
    <defs>
      <linearGradient id="photoTone" x1="0" y1="0" x2="0" y2="1">
        <stop offset="0" stop-color="#c9b79a"/>
        <stop offset="0.3" stop-color="#8a4b3a"/>
        <stop offset="0.7" stop-color="#7a4a38"/>
        <stop offset="1" stop-color="#4d6b34"/>
      </linearGradient>
      <linearGradient id="panelTone" x1="0" y1="0" x2="0" y2="1">
        <stop offset="0" stop-color="#3f8fd9"/>
        <stop offset="1" stop-color="#3a86d2"/>
      </linearGradient>
      <linearGradient id="officeTone" x1="0" y1="0" x2="0" y2="1">
        <stop offset="0" stop-color="#b7c6d6"/>
        <stop offset="0.6" stop-color="#8d3b34"/>
        <stop offset="1" stop-color="#6f6a66"/>
      </linearGradient>
      <linearGradient id="conservatoryTone" x1="0" y1="0" x2="0" y2="1">
        <stop offset="0" stop-color="#d8dde4"/>
        <stop offset="0.7" stop-color="#f1f1ee"/>
        <stop offset="1" stop-color="#5f7a3e"/>
      </linearGradient>
      <linearGradient id="vanTone" x1="0" y1="0" x2="0" y2="1">
        <stop offset="0" stop-color="#4f6b3a"/>
        <stop offset="0.45" stop-color="#e9ecef"/>
        <stop offset="1" stop-color="#8a8f94"/>
      </linearGradient>
    </defs>

    <g role="img" aria-label="Photo: a window cleaner in a blue polo shirt using a water-fed pole on the windows of a red-brick Tudor-style house with rose bushes">
      <rect x="0" y="0" width="900" height="700" fill="url(#photoTone)"/>
    </g>

    <path d="M0,0 H486 C430,120 290,192 110,188 C65,187 28,183 0,178 Z" fill="var(--navy)"/>
    <path d="M0,0 H480 C424,114 284,180 110,176 C64,175 28,170 0,164 Z" fill="var(--sky)"/>
    <path d="M0,0 H470 C412,108 272,166 105,162 C58,161 26,157 0,150 Z" fill="var(--white)"/>

    <path d="M0,498 C80,540 170,598 280,603 C360,606 430,590 520,560 L520,1200 L0,1200 Z" fill="var(--sky)"/>
    <path d="M0,512 C80,552 170,608 280,613 C360,616 430,600 520,572 L520,1200 L0,1200 Z" fill="url(#panelTone)"/>

    <path d="M382,650 C430,600 470,585 520,568 C620,530 730,478 800,476 C850,476 885,488 900,498 L900,1200 L498,1200 C500,1040 470,760 382,650 Z" fill="var(--sky)"/>
    <path d="M388,660 C436,612 476,596 526,580 C626,544 736,500 800,500 C846,501 880,530 900,566 L900,1200 L498,1200 C500,1046 472,764 388,660 Z" fill="var(--navy)"/>
    <path d="M392,668 C440,622 480,606 530,592 C630,560 736,520 800,520 C848,520 882,545 900,575 L900,1200 L505,1200 C506,1052 478,770 392,668 Z" fill="var(--white)"/>
    <path d="M392,668 C470,760 500,1000 503,1200" fill="none" stroke="var(--white)" stroke-width="6"/>

    <path d="M140,1200 C240,1135 380,1112 498,1110 C640,1108 780,1150 872,1200 Z" fill="var(--navy)"/>
    <path d="M140,1200 C240,1138 380,1116 498,1114 C630,1113 760,1152 836,1200 Z" fill="var(--sky)"/>
    <path d="M140,1200 C240,1142 380,1121 498,1120 C620,1120 730,1158 800,1200 Z" fill="var(--white)"/>

    <g role="img" aria-label="Photo: cleaner working on an office building with large shop-front windows">
      <circle cx="107" cy="611" r="75" fill="url(#officeTone)" stroke="var(--navy)" stroke-width="3"/>
    </g>
    <g role="img" aria-label="Photo: white conservatory with clean glass panes">
      <circle cx="262" cy="619" r="62" fill="url(#conservatoryTone)" stroke="var(--navy)" stroke-width="3"/>
    </g>
    <g role="img" aria-label="Photo: the company's white service van">
      <circle cx="396" cy="608" r="54" fill="url(#vanTone)" stroke="var(--navy)" stroke-width="3"/>
    </g>

    <path d="M0,705 H247 L256,712 L247,732 H0 Z" fill="var(--sky)"/>
    <path d="M0,705 H240 L249,712 L240,732 H0 Z" fill="var(--navy)"/>
    <path d="M0,924 H247 L256,931 L247,952 H0 Z" fill="var(--sky)"/>
    <path d="M0,924 H240 L249,931 L240,952 H0 Z" fill="var(--navy)"/>
  </svg>

  <div class="brand">
    <span class="brand-name">LUNAR SWEEP</span>
    <span class="brand-sub">CLEANING &amp; MAINTENANCE LTD</span>
  </div>

  <h2 class="section-title about-title">ABOUT LUNAR SWEEP</h2>
  <p class="body-copy about-copy-1">Lunar Sweep Cleaning Ltd have been cleaning windows for<br>commercial and residential properties throughout Hutton,<br>Shenfield and the surrounding areas since 1999. We cover<br>most towns in Essex including Brentwood, Chelmsford,<br>Romford, Loughton and Billericay.</p>
  <p class="body-copy about-copy-2">When it comes to window cleaning, we believe in giving our<br>clients the best possible service and that is why we were the first<br>window cleaning business in Brentwood to use the Pure Water<br>Fed Pole Systems, alongside traditional ladders and hand tools.</p>

  <h2 class="section-title why-title">WHY LUNAR SWEEP</h2>
  <p class="body-copy why-copy">Pure Water Fed Pole Systems are the future for the window cleaning<br>industry, as they comply with Health and Safety Laws. They also offer<br>lots of other benefits for our customers including:</p>
  <ul class="benefits">
    <li><svg viewBox="0 0 12 12"><circle cx="6" cy="6" r="6" fill="#fff"/><path d="M3.2,6.2 L5.2,8 L8.8,4.2" fill="none" stroke="#3c8ad5" stroke-width="1.6" stroke-linecap="round" stroke-linejoin="round"/></svg>REDUCES DISTURBANCE TO BUILDING OCCUPANTS</li>
    <li><svg viewBox="0 0 12 12"><circle cx="6" cy="6" r="6" fill="#fff"/><path d="M3.2,6.2 L5.2,8 L8.8,4.2" fill="none" stroke="#3c8ad5" stroke-width="1.6" stroke-linecap="round" stroke-linejoin="round"/></svg>CLEANING UP TO 50 FEET FROM THE SAFETY OF THE GROUND</li>
    <li><svg viewBox="0 0 12 12"><circle cx="6" cy="6" r="6" fill="#fff"/><path d="M3.2,6.2 L5.2,8 L8.8,4.2" fill="none" stroke="#3c8ad5" stroke-width="1.6" stroke-linecap="round" stroke-linejoin="round"/></svg>FRAMES CLEANED AS STANDARD</li>
    <li><svg viewBox="0 0 12 12"><circle cx="6" cy="6" r="6" fill="#fff"/><path d="M3.2,6.2 L5.2,8 L8.8,4.2" fill="none" stroke="#3c8ad5" stroke-width="1.6" stroke-linecap="round" stroke-linejoin="round"/></svg>CLEANING OF WINDOWS THAT LADDERS COULD NOT REACH</li>
    <li><svg viewBox="0 0 12 12"><circle cx="6" cy="6" r="6" fill="#fff"/><path d="M3.2,6.2 L5.2,8 L8.8,4.2" fill="none" stroke="#3c8ad5" stroke-width="1.6" stroke-linecap="round" stroke-linejoin="round"/></svg>REDUCES THE COST OF WINDOW CLEANING.</li>
  </ul>

  <h1 class="headline">
    <span class="headline-kicker">RELIABLE</span>
    <span class="headline-kicker">RESIDENTIAL &amp; COMMERCIAL</span>
    <span class="headline-main">WINDOW</span>
    <span class="headline-main">CLEANING</span>
    <span class="headline-main accent">IN ESSEX</span>
  </h1>

  <p class="offer">WE ARE HAPPY TO PROVIDE<br>FREE, FRIENDLY ADVICE AND<br>AN ON SITE DEMONSTRATION OF OUR<br>WINDOW CLEANING CAPABILITIES.</p>

  <div class="cta">CONTACT US TODAY!</div>

  <ul class="contact-list">
    <li><svg viewBox="0 0 12 12"><path d="M2.5,1 L4.5,1 L5.3,3.6 L4,4.6 C4.6,6 5.9,7.4 7.4,8 L8.4,6.7 L11,7.5 L11,9.5 C11,10.4 10.3,11 9.4,11 C5,10.6 1.4,7 1,2.6 C1,1.7 1.6,1 2.5,1 Z" fill="#3c8ad5"/></svg>Office:&nbsp; 01394528160</li>
    <li><svg viewBox="0 0 12 12"><path d="M2.5,1 L4.5,1 L5.3,3.6 L4,4.6 C4.6,6 5.9,7.4 7.4,8 L8.4,6.7 L11,7.5 L11,9.5 C11,10.4 10.3,11 9.4,11 C5,10.6 1.4,7 1,2.6 C1,1.7 1.6,1 2.5,1 Z" fill="#3c8ad5"/></svg>Mobile: 07821563047</li>
    <li><svg viewBox="0 0 12 12"><rect x="0.5" y="2.5" width="11" height="7.5" fill="#3c8ad5"/><path d="M0.8,2.8 L6,7 L11.2,2.8" fill="none" stroke="#fff" stroke-width="1"/></svg>lunarsweep@postmerin.co.uk</li>
  </ul>

  <p class="website">www.lunarsweep.ltd</p>
</div>
</body>
</html>
```